Builders Worksite Corflute Outdoor Sign

We are a building company who are just branching out into new construction. How first new build is our own home which was designed by us and a local architect. We are proud and want to create more advertisement around our business.

We need a corflute sign that can staked outside the construction site and can be seen by people passing by.
Updates

Can we please make the company name and logo bigger (Tidewater Ridge Homes) This needs to be the focus. Can we please replace 'Manu' with 'Contact Us on 021-574-3619'

Target Market(s)

Home owners and people wishing to build on lifestyle blocks in New Zealand.

Font styles to use
Sans Serif

Requirements
Must have
• It needs to feature our:
Logo
Company name
Contact name and number - Manu - 0215743619
Landscape NOT portrait.

```html
<!DOCTYPE html>
<html lang="en">
<head>
<meta charset="utf-8">
<title>Tidewater Ridge Homes – Worksite Sign</title>
<link rel="stylesheet" href="https://fonts.googleapis.com/css2?family=Jost:wght@400&family=Roboto+Condensed:wght@800&family=Roboto+Slab:wght@700&display=swap">
<style>
  :root {
    --backdrop: #98999a;
    --sign-white: #ffffff;
    --backdrop-grey: #b5b7c2;
    --backdrop-grey-soft: #d3d5dc;
    --navy: #070d22;
    --sign-yellow: #fbbf22;
  }
  * { margin: 0; padding: 0; box-sizing: border-box; }
  html, body {
    width: 800px;
    height: 1200px;
    overflow: hidden;
    background: var(--backdrop);
  }
  .canvas {
    position: relative;
    width: 800px;
    height: 1200px;
  }
  .sign {
    position: absolute;
    left: 40px;
    top: 360px;
    width: 720px;
    height: 480px;
    background: var(--sign-white);
    overflow: hidden;
  }
  .sign__backdrop {
    position: absolute;
    left: 10px;
    top: 0;
    width: 700px;
    height: 328px;
    background: radial-gradient(ellipse 60% 70% at 50% 100%, var(--backdrop-grey-soft) 0%, var(--backdrop-grey) 100%);
  }
  .brand {
    position: absolute;
    left: 0; right: 0;
    top: 98px;
    text-align: center;
    color: var(--navy);
    font-family: "Jost", sans-serif;
    font-weight: 400;
  }
  .brand__row {
    display: flex;
    justify-content: center;
    align-items: center;
    gap: 14px;
  }
  .brand__mark {
    width: 46px;
    height: 46px;
    border-radius: 50%;
    background: var(--sign-yellow);
    flex: none;
  }
  .brand__name {
    font-size: 60px;
    line-height: 1;
    letter-spacing: 0.5px;
    white-space: nowrap;
  }
  .brand__tagline {
    margin-top: 26px;
    font-size: 50px;
    line-height: 1;
    letter-spacing: 30px;
    padding-left: 30px;
  }
  .sign__rule {
    position: absolute;
    left: 0;
    top: 325px;
    width: 720px;
    height: 6px;
    background: var(--navy);
  }
  .sign__contact-band {
    position: absolute;
    left: 0;
    top: 331px;
    width: 720px;
    height: 149px;
    background: var(--sign-yellow);
  }
  .contact-pill {
    position: absolute;
    left: 170px;
    top: 295px;
    width: 378px;
    height: 64px;
    border-radius: 32px;
    background: var(--navy);
    color: var(--sign-white);
    font-family: "Roboto Slab", serif;
    font-weight: 700;
    font-size: 42px;
    line-height: 64px;
    text-align: center;
  }
  .phone {
    position: absolute;
    left: 77px;
    top: 389px;
    height: 70px;
    display: flex;
    align-items: center;
    gap: 32px;
  }
  .phone__icon { width: 70px; height: 70px; flex: none; }
  .phone__number {
    font-family: "Roboto Condensed", sans-serif;
    font-weight: 800;
    font-size: 84px;
    line-height: 1;
    color: var(--navy);
    letter-spacing: 0;
  }
</style>
</head>
<body>
<main class="canvas">
  <section class="sign" aria-label="Tidewater Ridge Homes worksite sign">
    <div class="sign__backdrop" role="img" aria-label="Brand backdrop graphic in soft grey"></div>
    <div class="brand">
      <div class="brand__row">
        <span class="brand__mark" aria-hidden="true"></span>
        <span class="brand__name">TIDEWATER RIDGE</span>
      </div>
      <div class="brand__tagline">HOMES</div>
    </div>
    <div class="sign__rule"></div>
    <div class="sign__contact-band"></div>
    <div class="contact-pill">Contact Manu</div>
    <div class="phone">
      <svg class="phone__icon" viewBox="0 0 70 70" aria-hidden="true">
        <circle cx="35" cy="35" r="35" fill="var(--navy)"/>
        <path d="M24 19c2-1 4-1 5 1l4 7c1 2 0 3-1 4l-3 2c2 5 6 9 11 11l2-3c1-1 3-2 4-1l7 4c2 1 2 3 1 5l-2 3c-2 2-5 3-8 2-11-4-19-12-23-23-1-3 0-6 2-8z" fill="none" stroke="var(--sign-white)" stroke-width="4" stroke-linejoin="round"/>
        <path d="M39 22a10 10 0 0 1 9 9" fill="none" stroke="var(--sign-white)" stroke-width="3" stroke-linecap="round"/>
        <path d="M40 15a17 17 0 0 1 15 15" fill="none" stroke="var(--sign-white)" stroke-width="3" stroke-linecap="round"/>
      </svg>
      <span class="phone__number">0215743619</span>
    </div>
  </section>
</main>
</body>
</html>
```